Certificate Design for Employee Loyalty

We're a digital marketing agency in Australia (www.tidewavestudio.com.au) and we're looking to create a design for a certificate to celebrate employees who reach 5 years with us (we have a few coming up soon).
Ideally we'd want something that captures our funky, digital agency culture (see our Chatterloop page www.chatterloop.net/tidewavestudio for what we mean) and not be too "corporatey"
A4 portrait or landscape designs would be awesome, with spots for employee's name, a brief 2-3 line message and a design that reflects our culture and the 5 year milestone for the employee.
Any questions, please post!
Digital marketing employees.
Landscape

```html
<!DOCTYPE html>
<html lang="en">
<head>
<meta charset="utf-8">
<title>Tidewave Studio – Certificate of Achievement for Employee Loyalty</title>
<link rel="stylesheet" href="https://fonts.googleapis.com/css2?family=IM+Fell+English&family=Questrial&family=Great+Vibes&display=swap">
<style>
  :root {
    --backdrop: #8c8c90;
    --paper: #a9a9ac;
    --paper-light: #b4b4b7;
    --ink: #111111;
    --ink-soft: #3a3a3a;
    --muted: #8a8a8e;
    --accent-blue: #2f86c6;
    --rule: #6e6e72;
    --white: #ffffff;
  }
  * { margin: 0; padding: 0; box-sizing: border-box; }
  html, body {
    width: 1200px; height: 1000px; overflow: hidden;
    background: var(--backdrop);
  }
  .canvas {
    position: relative; width: 1200px; height: 1000px;
    display: flex; align-items: center; justify-content: center;
  }
  .certificate {
    position: relative; width: 960px; height: 680px;
    background: linear-gradient(180deg, var(--paper-light), var(--paper));
    box-shadow: 0 10px 24px rgba(0,0,0,.35);
    overflow: hidden;
  }
  .certificate__title {
    position: absolute; top: 40px; left: 0; width: 100%;
    text-align: center;
    font-family: "IM Fell English", Georgia, serif;
    font-size: 74px; font-weight: 400; color: var(--ink);
    letter-spacing: 1px;
    text-shadow: 2px 2px 0 var(--white);
  }
  .title-band {
    position: absolute; top: 136px; left: 0; width: 100%; height: 26px;
    background: linear-gradient(90deg, #c9c9cc 0%, #2a2a2a 14%, var(--ink) 40%, var(--ink) 100%);
  }
  .title-band__for {
    position: absolute; left: 50%; top: -12px; transform: translateX(-90px);
    font-family: "Great Vibes", cursive; font-size: 38px; color: var(--white);
  }
  .certificate__subject {
    position: absolute; top: 178px; left: 0; width: 100%;
    text-align: center;
    font-family: "Questrial", Arial, sans-serif; font-size: 54px; color: var(--ink);
  }
  .recipient {
    position: absolute; top: 256px; left: 230px; width: 470px; text-align: center;
    font-family: "Questrial", Arial, sans-serif;
  }
  .recipient__name { font-size: 30px; color: var(--muted); line-height: 1.1; }
  .recipient__rule { height: 1px; background: var(--rule); margin: 2px 0 4px; }
  .recipient__milestone { font-size: 26px; color: var(--accent-blue); letter-spacing: 1px; }
  .flourish {
    position: absolute; top: 350px; left: 340px; width: 250px; height: 70px;
    background: radial-gradient(ellipse at center, rgba(40,40,40,.35), rgba(40,40,40,0) 70%);
  }
  .message-lines {
    position: absolute; top: 430px; left: 355px; width: 290px;
  }
  .message-lines span {
    display: block; height: 1px; background: var(--rule); margin-bottom: 30px;
  }
  .team-figures {
    position: absolute; top: 370px; left: 90px; width: 210px; height: 290px;
    background: linear-gradient(180deg, #1c1c1c, #000);
    border-radius: 60px 60px 6px 6px;
  }
  .seal {
    position: absolute; top: 318px; left: 690px; width: 200px; height: 200px;
  }
  .brand {
    position: absolute; top: 540px; left: 380px; width: 400px;
    display: flex; align-items: center; justify-content: center; gap: 12px;
    font-family: "Questrial", Arial, sans-serif; font-size: 44px; line-height: 1; color: var(--ink);
    white-space: nowrap;
  }
  .brand__dot {
    flex: none; width: 24px; height: 24px; border-radius: 50%; background: var(--accent-blue);
  }
  .footer-bands { position: absolute; left: 0; bottom: 0; width: 100%; height: 70px; }
  .footer-bands__thick { position: absolute; top: 0; left: 0; width: 100%; height: 8px; background: var(--ink); }
  .footer-bands__sheen {
    position: absolute; top: 8px; left: 0; width: 100%; height: 40px;
    background: linear-gradient(180deg, #7a7a7d, var(--paper));
  }
  .footer-bands__thin { position: absolute; top: 52px; left: 0; width: 100%; height: 3px; background: var(--ink-soft); }
</style>
</head>
<body>
<main class="canvas">
  <section class="certificate">
    <h1 class="certificate__title">Certificate of Achievement</h1>
    <div class="title-band"><span class="title-band__for">for</span></div>
    <h2 class="certificate__subject">Employee Loyalty</h2>

    <div class="recipient">
      <p class="recipient__name">(Name)</p>
      <div class="recipient__rule"></div>
      <p class="recipient__milestone">riding 5 tides</p>
    </div>

    <div class="flourish" role="img" aria-label="Decorative calligraphic flourish beneath the name"></div>

    <div class="message-lines"><span></span><span></span><span></span></div>

    <div class="footer-bands">
      <div class="footer-bands__thick"></div>
      <div class="footer-bands__sheen"></div>
      <div class="footer-bands__thin"></div>
    </div>

    <div class="team-figures" role="img" aria-label="Black silhouettes of three team members standing together"></div>

    <svg class="seal" viewBox="0 0 200 200" aria-label="Plain award seal">
      <defs>
        <radialGradient id="sealRing" cx="50%" cy="45%" r="60%">
          <stop offset="0%" stop-color="#f2f2f2"/>
          <stop offset="60%" stop-color="#6a6a6a"/>
          <stop offset="100%" stop-color="#2b2b2b"/>
        </radialGradient>
        <linearGradient id="sealFace" x1="0" y1="0" x2="1" y2="1">
          <stop offset="0%" stop-color="#5a5a5a"/>
          <stop offset="50%" stop-color="#e8e8e8"/>
          <stop offset="100%" stop-color="#6a6a6a"/>
        </linearGradient>
      </defs>
      <circle cx="100" cy="100" r="96" fill="#333"/>
      <circle cx="100" cy="100" r="88" fill="url(#sealRing)"/>
      <circle cx="100" cy="100" r="62" fill="url(#sealFace)"/>
      <circle cx="100" cy="100" r="70" fill="none" stroke="#111" stroke-width="2" stroke-dasharray="6 4"/>
    </svg>

    <div class="brand"><span>tidewave studio</span><span class="brand__dot"></span></div>
  </section>
</main>
</body>
</html>
```